Tallow Bright business card

Tallow Bright is a new online life insurance company providing instant quotes and policies to consumers.
Target Market(s)
Target market is both business to business as well as business to consumer
Can think out side of the box- We are an open minded bunch
Industry/Entity Type
Life Insurance
Requirements
Must have
- Our corporate Logo
Double sided
Website www.tallowbright.com.au
Phone Number
Name & Position of each person etc.
Modern font

```html
<!DOCTYPE html>
<html lang="en">
<head>
<meta charset="utf-8">
<title>Tallow Bright business card</title>
<link rel="stylesheet" href="https://fonts.googleapis.com/css2?family=Carlito:wght@400;700&display=swap">
<style>
  :root {
    --ink: #000000;
    --paper: #ffffff;
    --accent: #f26a10;
  }
  * { box-sizing: border-box; margin: 0; padding: 0; }
  html, body {
    width: 876px;
    height: 1200px;
    overflow: hidden;
    background: var(--paper);
    font-family: "Carlito", "Calibri", sans-serif;
    color: var(--ink);
  }
  .canvas { position: relative; width: 876px; height: 1200px; }

  .card {
    position: absolute;
    left: 7px;
    width: 866px;
    height: 524px;
    border: 3px solid var(--ink);
    background: var(--paper);
  }
  .card--front { top: 7px; }
  .card--back { top: 673px; }

  .title-bar {
    position: absolute;
    left: 0; top: 0; right: 0;
    height: 40px;
    background: var(--ink);
  }
  .title-bar__url {
    position: absolute;
    left: 22px;
    top: 5px;
    font-size: 26px;
    line-height: 30px;
    color: var(--accent);
    letter-spacing: 0.2px;
  }
  .window-controls {
    position: absolute;
    right: 6px;
    top: 5px;
    display: flex;
    gap: 14px;
  }
  .window-controls svg { display: block; width: 34px; height: 32px; }

  .brand {
    position: absolute;
    display: flex;
    align-items: center;
    gap: 14px;
    font-weight: 700;
    color: var(--ink);
    white-space: nowrap;
  }
  .brand__dot {
    border-radius: 50%;
    background: var(--accent);
    flex: none;
  }
  .brand--hero { left: 0; right: 0; justify-content: center; top: 205px; font-size: 92px; line-height: 100px; }
  .brand--hero .brand__dot { width: 34px; height: 34px; }
  .brand--small { left: 24px; top: 408px; font-size: 44px; line-height: 50px; gap: 8px; }
  .brand--small .brand__dot { width: 17px; height: 17px; }

  .person { position: absolute; left: 24px; top: 107px; }
  .person__name { font-size: 31px; font-weight: 700; line-height: 36px; }
  .person__role { font-size: 24px; font-weight: 700; line-height: 32px; }

  .contact {
    position: absolute;
    right: 21px;
    text-align: right;
    font-size: 24px;
    line-height: 33px;
  }
  .contact--address { top: 108px; }
  .contact--lines { top: 232px; }
</style>
</head>
<body>
<main class="canvas">

  <section class="card card--front" aria-label="Card front">
    <header class="title-bar">
      <span class="title-bar__url">www.tallowbright.com.au</span>
      <div class="window-controls" aria-hidden="true">
        <svg viewBox="0 0 34 32"><rect x="1.5" y="1.5" width="31" height="29" rx="6" fill="none" stroke="#fff" stroke-width="3"/><rect x="10" y="20" width="13" height="4" fill="#fff"/></svg>
        <svg viewBox="0 0 34 32"><rect x="1.5" y="1.5" width="31" height="29" rx="6" fill="none" stroke="#fff" stroke-width="3"/><rect x="8.5" y="8" width="17" height="16" fill="none" stroke="#fff" stroke-width="2.5"/><rect x="8.5" y="8" width="17" height="4" fill="#fff"/></svg>
        <svg viewBox="0 0 34 32"><rect x="1.5" y="1.5" width="31" height="29" rx="6" fill="none" stroke="#fff" stroke-width="3"/><path d="M10 9 L24 23 M24 9 L10 23" stroke="#fff" stroke-width="3.5" stroke-linecap="round"/></svg>
      </div>
    </header>
    <div class="brand brand--hero">
      <span class="brand__name">Tallow Bright</span>
      <span class="brand__dot" aria-hidden="true"></span>
    </div>
  </section>

  <section class="card card--back" aria-label="Card back">
    <header class="title-bar">
      <span class="title-bar__url">www.tallowbright.com.au</span>
      <div class="window-controls" aria-hidden="true">
        <svg viewBox="0 0 34 32"><rect x="1.5" y="1.5" width="31" height="29" rx="6" fill="none" stroke="#fff" stroke-width="3"/><rect x="10" y="20" width="13" height="4" fill="#fff"/></svg>
        <svg viewBox="0 0 34 32"><rect x="1.5" y="1.5" width="31" height="29" rx="6" fill="none" stroke="#fff" stroke-width="3"/><rect x="8.5" y="8" width="17" height="16" fill="none" stroke="#fff" stroke-width="2.5"/><rect x="8.5" y="8" width="17" height="4" fill="#fff"/></svg>
        <svg viewBox="0 0 34 32"><rect x="1.5" y="1.5" width="31" height="29" rx="6" fill="none" stroke="#fff" stroke-width="3"/><path d="M10 9 L24 23 M24 9 L10 23" stroke="#fff" stroke-width="3.5" stroke-linecap="round"/></svg>
      </div>
    </header>

    <div class="person">
      <p class="person__name">Maren Ashcroft</p>
      <p class="person__role">Sales Manager</p>
    </div>

    <address class="contact contact--address" style="font-style:normal">
      Level 18, 42 Harbour Lane<br>
      Northvale NSW 2065
    </address>

    <div class="contact contact--lines">
      <p>phone: +555 1300 820 410</p>
      <p>fax: +555 1300 820 411</p>
      <p>maren@tallowbright.com.au</p>
    </div>

    <div class="brand brand--small">
      <span class="brand__name">Tallow Bright</span>
      <span class="brand__dot" aria-hidden="true"></span>
    </div>
  </section>

</main>
</body>
</html>
```